Design for Employee Baseball Cards

Looking to design baseball cards for my employees. Trying to replicate famous baseball card design with swapping in an employee and listing there stats and fun facts. These cards will be inserted into boxes so customers can receive with their orders. Cards allow customers to put a face to the name they've always corresponded with, which makes their experience personable and more memorable.

Looking for a front and back design template. We are open to the design, but would like it to resemble a baseball/playing card.
Size: 2.5" x 3.5" vertical
Here is our website which can be referenced for color pallet and tone.
https://www.crateswithmarlow.com/

Attached is an example of a vintage baseball. Can we see some versions like this?

Front
- Person's name
- Title/Department
- Crates With Marlow logo
- Person's photo - this will be an action shot like a baseball card

Back
I'm open to the design and content of the back. We want it to resemble a back of a baseball card as best as possible. Normally, baseball cards will have stats by year. Instead, we can have stats and fun facts like the following

Items for Back
- Bio
- Year started at CWM
- Department
- Years of experience
- Specialty
- Secret skill
- What you love about CWM
- Favorite quote
- Fun fact
- Passion outside of CWM
- Person's photo - we can include a smaller headshot

Font styles to use
Sans Serif

Colors
0054AA
0677BA
7BADD7
CADEEF
E8F1F8

Requirements
Must have
• The deliverable must be a template PSD or AI that we can swap in photos and edit text for each person's card.

```html
<!DOCTYPE html>
<html lang="en">
<head>
<meta charset="utf-8">
<title>Employee Baseball Card – Front and Back</title>
<link rel="stylesheet" href="https://fonts.googleapis.com/css2?family=Montserrat:ital,wght@0,600;0,700;0,800;1,700;1,800&family=Lato:wght@400;700&display=swap">
<style>
  :root {
    --brand-blue: #0054aa;
    --mid-blue: #0677ba;
    --sky-blue: #7badd7;
    --pale-blue: #cadeef;
    --mist-blue: #e8f1f8;
    --white: #ffffff;
    --backdrop: #b4b5b9;
    --photo-green-light: #7e9b72;
    --photo-green-dark: #557a4b;
  }
  * { box-sizing: border-box; margin: 0; padding: 0; }
  html, body { width: 1200px; height: 1200px; overflow: hidden; }
  body {
    background: var(--backdrop);
    position: relative;
    font-family: "Lato", sans-serif;
  }
  .card {
    position: absolute;
    top: 241px;
    width: 512px;
    height: 716px;
    background: var(--brand-blue);
    overflow: hidden;
  }
  .card--front { left: 70px; }
  .card--back { left: 610px; }

  /* FRONT */
  .action-photo {
    position: absolute;
    left: 24px; top: 24px;
    width: 464px; height: 670px;
    background: linear-gradient(180deg, var(--photo-green-light) 0%, var(--photo-green-dark) 100%);
  }
  .name-banner {
    position: absolute;
    left: 155px; top: 24px;
    width: 333px; height: 58px;
  }
  .name-banner svg { position: absolute; inset: 0; }
  .name-banner__text {
    position: absolute;
    right: 10px; top: 3px;
    font-family: "Montserrat", sans-serif;
    font-weight: 800; font-style: italic;
    font-size: 43px; line-height: 50px;
    color: var(--white);
    white-space: nowrap;
  }
  .brand-tag {
    position: absolute;
    left: 360px; top: 80px;
    width: 128px; height: 55px;
    background: var(--white);
    display: flex; align-items: center; gap: 6px;
    padding: 0 6px;
  }
  .brand-tag__square {
    width: 14px; height: 14px; flex: none;
    background: var(--brand-blue);
  }
  .brand-tag__name {
    font-family: "Lato", sans-serif;
    font-weight: 400;
    font-size: 15px; line-height: 16px;
    color: var(--brand-blue);
  }
  .department-banner {
    position: absolute;
    left: 24px; top: 640px;
    width: 345px; height: 56px;
  }
  .department-banner svg { position: absolute; inset: 0; }
  .department-banner__text {
    position: absolute;
    left: 6px; top: 3px;
    font-family: "Montserrat", sans-serif;
    font-weight: 800; font-style: italic;
    font-size: 42px; line-height: 50px;
    color: var(--white);
    white-space: nowrap;
  }

  /* BACK */
  .back-hero {
    position: absolute;
    left: 0; top: 0;
    width: 512px; height: 300px;
    background: linear-gradient(180deg, #b9cbe0 0%, #6f96c4 22%, #2f6db3 55%, var(--brand-blue) 100%);
  }
  .bio-label {
    position: absolute;
    left: 85px; top: 24px;
    font-family: "Montserrat", sans-serif;
    font-weight: 700; font-style: italic;
    font-size: 15px;
    color: var(--white);
  }
  .bio-label svg { position: absolute; left: 30px; top: 12px; }
  .bio-text {
    position: absolute;
    left: 28px; top: 62px;
    font-size: 14.5px; line-height: 26px;
    color: var(--white);
    white-space: nowrap;
  }
  .bio-text span { display: block; }
  .headshot {
    position: absolute;
    left: 315px; top: 23px;
    width: 168px; height: 223px;
    border: 4px solid var(--white);
    background: linear-gradient(180deg, #5f86b5 0%, #7a9cc4 45%, #e9e6e2 85%, #f4f4f4 100%);
  }
  .back-name {
    position: absolute;
    right: 28px; top: 240px;
    padding: 0 0 0 10px;
    background: var(--brand-blue);
    font-family: "Montserrat", sans-serif;
    font-weight: 800; font-style: italic;
    font-size: 40px; line-height: 48px;
    color: var(--white);
    white-space: nowrap;
  }
  .stat-list {
    position: absolute;
    left: 28px; top: 317px;
    width: 454px;
    list-style: none;
  }
  .stat-row {
    height: 30px;
    margin-bottom: 12.7px;
    background: var(--white);
    border-radius: 4px;
    padding-left: 11px;
    display: flex; align-items: center;
    font-family: "Montserrat", sans-serif;
    font-weight: 700;
    font-size: 11px;
    color: var(--brand-blue);
  }
</style>
</head>
<body>

<section class="card card--front" aria-label="Card front">
  <div class="action-photo" role="img" aria-label="Action photo of the employee swinging a baseball bat on a ball field"></div>

  <div class="name-banner">
    <svg width="333" height="58" viewBox="0 0 333 58" aria-hidden="true">
      <polygon points="14,0 333,0 333,58 0,58" fill="var(--brand-blue)"/>
      <polyline points="14,0 0,58 333,58" fill="none" stroke="var(--white)" stroke-width="5"/>
    </svg>
    <h1 class="name-banner__text">EVAN HALE</h1>
  </div>

  <div class="brand-tag">
    <span class="brand-tag__square"></span>
    <span class="brand-tag__name">Crates With Marlow</span>
  </div>

  <div class="department-banner">
    <svg width="345" height="56" viewBox="0 0 345 56" aria-hidden="true">
      <polygon points="0,0 345,0 333,56 0,56" fill="var(--brand-blue)"/>
      <polyline points="0,3 343,3 332,48" fill="none" stroke="var(--white)" stroke-width="4"/>
    </svg>
    <h2 class="department-banner__text">DEPARTMENT</h2>
  </div>
</section>

<section class="card card--back" aria-label="Card back">
  <div class="back-hero" aria-hidden="true"></div>

  <div class="bio-label">BIO
    <svg width="12" height="12" viewBox="0 0 12 12" aria-hidden="true">
      <path d="M2 2 L9 9 M9 4 L9 9 L4 9" fill="none" stroke="var(--white)" stroke-width="1.2"/>
    </svg>
  </div>
  <p class="bio-text">
    <span>Lorem ipsum dolor sit amet, consectet</span>
    <span>ur adipiscing elit, sed do eiusmod temp</span>
    <span>or incididunt ut labore et dolore magna</span>
    <span>aliua. Ut enim ad minim veniam, quis no</span>
    <span>strd exercitation ullamco laboris nisi ut a</span>
    <span>iquip ex ea commodo consequat.</span>
  </p>

  <div class="headshot" role="img" aria-label="Headshot of the employee in a ball cap and pinstripe jersey"></div>
  <h2 class="back-name">EVAN HALE</h2>

  <ul class="stat-list">
    <li class="stat-row">Year started at CWM :</li>
    <li class="stat-row">Department :</li>
    <li class="stat-row">Years of experience :</li>
    <li class="stat-row">Specialty :</li>
    <li class="stat-row">Secret skill :</li>
    <li class="stat-row">What you love about CWM :</li>
    <li class="stat-row">Favorite quote :</li>
    <li class="stat-row">Fun fact :</li>
    <li class="stat-row">Passion outside of CWM :</li>
  </ul>
</section>

</body>
</html>
```